THE GRAND DELTA GROOVE REVUE---a CONCERT

We need a web page to support our upcoming concert asap. It is a southern blues concert featuring Odessa Brantley, Whitfield, Marvell Gaddis, and Reuben Oakes. We have as special guest local talent from the Augusta, Ga Area---Calloway, Abe Lark and Jo'Vanna. Hosted By: Augusta's Own--Brave Pecan.
The concert is as follow:
The Grand Delta Groove Revue
Saturday, July 7, 2018
7:00 pm Doors open at 6:00pm
Harlow Civic Hall, Augusta, GA
Tickets are $39, $49 and $59
Tickets on sale at the Box Office(need link to "BUY TICKETS"), Zenith Records, Marigold Box Office and Camp Hollister, GA
We are honoring all military and first responders and offering discount tickets--contact 770-555-0182 for discount code
Overnight concert guests are invited to stay at the Restwell Lodge in Augusta for a reduced rate of $69--we would like a link to that site. Mention Code:
The Concert is promoted by QUARTZ MERIDIAN ENTERTAINMENT
Harlow Civic Hall Logo and Adress must appear somewhere at the bottom or near where Harlow Civic Hall is mentioned.
The Military requires that we say, No government or military endorsement implied.
Picture of the Artists and our current flyer is attached. If you need the layered file--contact us

Target Market(s)

blues music lovers and concert goers

Requirements
Must have
• link to buy tickets/mention chatterly and peepline
Nice to have
• links to artist sites and hotel, TICKET GIVEAWAY REGISTRATION

```html
<!DOCTYPE html>
<html lang="en">
<head>
<meta charset="utf-8">
<title>The Grand Delta Groove Revue</title>
<link href="https://fonts.googleapis.com/css2?family=Lato:wght@300;400&family=Oswald:wght@500&family=Cinzel:wght@700&display=swap" rel="stylesheet">
<style>
:root{
  --ink:#000;
  --white:#fff;
  --gold:#e9d08e;
  --gold-deep:#c9aa62;
  --btn-gold:#d8c184;
  --night:#0d1730;
  --steel:#4a5a7e;
}
*{box-sizing:border-box;margin:0;padding:0}
html,body{width:1125px;height:1200px;overflow:hidden;background:var(--ink)}
body{font-family:'Lato',sans-serif;color:var(--white);position:relative}
.hero{position:absolute;left:0;top:0;width:1125px;height:600px;overflow:hidden}
.hero-photo{position:absolute;inset:0;background:
  radial-gradient(ellipse at 25% 55%,#8a93ab 0%,rgba(74,90,126,.6) 30%,transparent 60%),
  radial-gradient(ellipse at 75% 30%,#24365f 0%,transparent 55%),
  linear-gradient(90deg,#5d6a88 0%,#1b2848 45%,var(--night) 100%)}
.brand{position:absolute;top:38px;left:0;width:100%;text-align:center;color:var(--gold);font-family:'Cinzel',serif;font-size:24px;line-height:1.25;letter-spacing:1px}
.event-date{position:absolute;top:205px;width:100%;text-align:center;font-size:31px;font-weight:400;letter-spacing:-1px}
.venue-title{position:absolute;top:235px;width:100%;text-align:center;font-family:'Cinzel',serif;font-size:46px;color:var(--gold);letter-spacing:1px}
.lineup{position:absolute;top:372px;left:160px;width:808px;display:flex;justify-content:space-between;font-family:'Oswald',sans-serif;color:var(--gold);text-align:center;text-transform:uppercase}
.artist{display:flex;flex-direction:column;align-items:center;line-height:1}
.artist .tag{font-size:20px;transform:scaleX(.8)}
.artist .name{font-size:38px;transform:scaleX(.8)}
.btn{display:inline-flex;align-items:center;justify-content:center;gap:8px;border-radius:18px;font-size:17px;letter-spacing:-.5px;text-decoration:none;height:32px}
.btn svg{width:16px;height:16px}
.btn-hero{position:absolute;top:496px;left:477px;width:170px;background:var(--btn-gold);color:#111}
.details{position:absolute;left:184px;top:697px;width:340px;font-size:13.5px;font-weight:300;line-height:19px;color:#e8e8e8}
.details p+p{margin-top:18px}
.actions{position:absolute;left:182px;top:928px;display:flex;gap:10px}
.btn-buy{width:171px;background:var(--white);color:#000}
.btn-call{width:146px;border:1.5px solid var(--white);color:var(--white)}
.artists-frame{position:absolute;left:580px;top:648px;width:382px;height:402px}
.artists-photo{position:absolute;left:-20px;top:18px;width:380px;height:362px;background:
  radial-gradient(ellipse at 55% 50%,#8a6a2e 0%,#3a2a1a 40%,transparent 70%),
  radial-gradient(ellipse at 45% 15%,#4a3cc0 0%,transparent 35%)}
.footer-brand{position:absolute;left:184px;top:1100px;color:var(--gold);font-family:'Cinzel',serif;font-size:13px;line-height:1.3;text-align:center;width:110px}
.footer-address{position:absolute;right:277px;top:1113px;font-size:15px;letter-spacing:.3px}
.social{position:absolute;left:886px;top:1112px;display:flex;gap:10px;font-size:12px}
.social a{display:flex;align-items:center;gap:4px;color:var(--white);text-decoration:none}
.social a::before{content:"";width:12px;height:12px;border-radius:50%;background:var(--white)}
</style>
</head>
<body>
<section class="hero">
  <div class="hero-photo" role="img" aria-label="Saxophone player in silhouette against a smoky blue stage with lights"></div>
  <div class="brand">THE GRAND DELTA<br>GROOVE REVUE</div>
  <div class="event-date">SATURDAY JULY 7, 2018</div>
  <h1 class="venue-title">HARLOW CIVIC HALL</h1>
  <div class="lineup">
    <div class="artist"><span class="tag">The Front Porch Man</span><span class="name">Marvell Gaddis</span></div>
    <div class="artist"><span class="name">Odessa</span><span class="name">"Bluebird" Brantley</span></div>
    <div class="artist"><span class="tag">The Legendary</span><span class="name">Whitfield</span></div>
    <div class="artist"><span class="name">Reuben Oakes</span><span class="tag">The Honey Drip Man</span></div>
  </div>
  <a class="btn btn-hero" href="#tickets"><svg viewBox="0 0 16 16"><path d="M1 2h2.5l2 8h7l1.5-6H5" fill="none" stroke="currentColor" stroke-width="1.8"/><circle cx="6.5" cy="13" r="1.4" fill="currentColor"/><circle cx="11.5" cy="13" r="1.4" fill="currentColor"/></svg>BUY TICKETS</a>
</section>

<section class="details">
  <p>We are honoring all military and first responders and offering discount tickets contact 770-555-0182 for discount code Overnight concert guests are invited to stay at the Restwell Lodge in Augusta for a reduced rate of $69</p>
  <p>The Grand Delta Groove Revue<br>Saturday, July 7, 2018<br>7:00 pm Doors open at 6:00pm<br>Harlow Civic Hall, Augusta, GA<br>Tickets are $39, $49 and $59</p>
</section>
<div class="actions" id="tickets">
  <a class="btn btn-buy" href="#tickets"><svg viewBox="0 0 16 16"><path d="M1 2h2.5l2 8h7l1.5-6H5" fill="none" stroke="currentColor" stroke-width="1.8"/><circle cx="6.5" cy="13" r="1.4" fill="currentColor"/><circle cx="11.5" cy="13" r="1.4" fill="currentColor"/></svg>BUY TICKETS</a>
  <a class="btn btn-call" href="tel:7705550182">CALL NOW</a>
</div>

<div class="artists-frame">
  <svg width="382" height="402" viewBox="0 0 382 402" style="position:absolute;inset:0"><path d="M0 0H382V402H256L248 395H375V7H7Z" fill="#fff"/></svg>
  <div class="artists-photo" role="img" aria-label="Group portrait of the four headlining artists"></div>
</div>

<footer>
  <div class="footer-brand">THE GRAND DELTA<br>GROOVE REVUE</div>
  <div class="footer-address">48 LARKSPUR AVE, AUGUSTA, GA 30904</div>
  <div class="social"><a href="#">chatterly</a><a href="#">peepline</a></div>
</footer>
</body>
</html>
```